The Perfect Business Card for PineHarbor

I am looking for a business card which beautifully incorporates my logo, reflects my business and looks special, elegant and clean.

```html
<!DOCTYPE html>
<html lang="en">
<head>
<meta charset="utf-8">
<title>PineHarbor Business Card</title>
<link rel="stylesheet" href="https://fonts.googleapis.com/css2?family=Cabin:wght@400;500&display=swap">
<style>
  :root {
    --page-bg: #ffffff;
    --card-white: #ffffff;
    --brand-green: #617a3a;
    --brand-green-text: #5d7a2e;
    --ink: #111111;
    --ink-dark-green: #1c2610;
    --faint-mark-light: #f0f2e8;
    --faint-glow-dark: rgba(150, 175, 110, 0.35);
    --on-green: #ffffff;
    --card-shadow: rgba(0, 0, 0, 0.35);
  }
  * { margin: 0; padding: 0; box-sizing: border-box; }
  html, body {
    width: 800px;
    height: 1200px;
    overflow: hidden;
    background: var(--page-bg);
    font-family: "Cabin", sans-serif;
  }
  .canvas { position: relative; width: 800px; height: 1200px; }

  .card {
    position: absolute;
    left: 120px;
    width: 560px;
    height: 320px;
    box-shadow: 4px 4px 6px var(--card-shadow);
    overflow: hidden;
  }
  .card-front { top: 180px; background: var(--card-white); }
  .card-back { top: 620px; background: var(--brand-green); }

  .front-watermark {
    position: absolute;
    left: 3px; top: 31px;
    width: 262px; height: 266px;
    border-radius: 50%;
    border: 2px solid var(--faint-mark-light);
    background: radial-gradient(circle at 55% 55%, #f6f8f0 0%, rgba(255,255,255,0) 60%);
  }
  .back-watermark {
    position: absolute;
    left: 410px; top: 0;
    width: 130px; height: 320px;
    background: radial-gradient(ellipse 50% 50% at 50% 60%, var(--faint-glow-dark) 0%, rgba(150,175,110,0) 100%);
  }

  .brand {
    position: absolute;
    display: flex;
    align-items: center;
    font-weight: 400;
    text-transform: uppercase;
    white-space: nowrap;
  }
  .brand-dot { border-radius: 50%; flex: none; }

  .card-front .brand {
    left: 298px; top: 45px;
    gap: 8px;
    color: var(--brand-green-text);
    font-size: 21px;
    letter-spacing: 0.5px;
  }
  .card-front .brand-dot { width: 63px; height: 63px; border: 1.5px solid var(--brand-green-text); }

  .card-back .brand {
    left: 53px; top: 52px;
    gap: 10px;
    color: var(--on-green);
    font-size: 30px;
    letter-spacing: 1px;
  }
  .card-back .brand-dot { width: 88px; height: 88px; border: 1.5px solid var(--on-green); }

  .contact-list {
    position: absolute;
    right: 63px;
    top: 175px;
    list-style: none;
  }
  .contact-item {
    display: flex;
    justify-content: flex-end;
    align-items: center;
    gap: 15px;
    height: 22.5px;
    font-size: 14px;
    color: var(--ink);
  }
  .contact-icon { width: 16px; height: 16px; flex: none; }

  .back-url {
    position: absolute;
    left: 53px;
    top: 233px;
    font-size: 12.5px;
    letter-spacing: 3.4px;
    color: var(--ink-dark-green);
  }
</style>
</head>
<body>
<main class="canvas">

  <section class="card card-front" aria-label="Business card front">
    <div class="front-watermark" role="img" aria-label="Large faint brand watermark"></div>
    <div class="brand">
      <span class="brand-dot" aria-hidden="true"></span>
      <span class="brand-name">PineHarbor</span>
    </div>
    <ul class="contact-list">
      <li class="contact-item">
        <span>+1 555 010 2468</span>
        <svg class="contact-icon" viewBox="0 0 24 24" aria-hidden="true"><path fill="#111" d="M6.6 10.8a15.1 15.1 0 0 0 6.6 6.6l2.2-2.2c.3-.3.7-.4 1-.2 1.1.4 2.3.6 3.6.6.6 0 1 .4 1 1V20c0 .6-.4 1-1 1A17 17 0 0 1 3 4c0-.6.4-1 1-1h3.5c.6 0 1 .4 1 1 0 1.3.2 2.5.6 3.6.1.3 0 .7-.2 1z"/></svg>
      </li>
      <li class="contact-item">
        <span>hello@pineharbormail.com</span>
        <svg class="contact-icon" viewBox="0 0 24 24" aria-hidden="true"><rect x="2" y="5" width="20" height="14" fill="#111"/><path d="M2 5l10 8 10-8M2 19l7.5-7M22 19l-7.5-7" stroke="#fff" stroke-width="1.6" fill="none"/></svg>
      </li>
      <li class="contact-item">
        <span>www.pineharborliving.com</span>
        <svg class="contact-icon" viewBox="0 0 24 24" aria-hidden="true"><circle cx="12" cy="12" r="10" fill="#111"/><g stroke="#fff" stroke-width="1.4" fill="none"><ellipse cx="12" cy="12" rx="4" ry="10"/><path d="M2 12h20M4 7h16M4 17h16"/></g></svg>
      </li>
    </ul>
  </section>

  <section class="card card-back" aria-label="Business card back">
    <div class="back-watermark" role="img" aria-label="Faint brand watermark"></div>
    <div class="brand">
      <span class="brand-dot" aria-hidden="true"></span>
      <span class="brand-name">PineHarbor</span>
    </div>
    <p class="back-url">www.pineharborliving.com</p>
  </section>

</main>
</body>
</html>
```